Business Cards for our company

Hi there,

we have successfully designed a logo with ArtFlock and would like now to design our business cards. We would like to keep the colours and the look-and-feel of the logo. Please send in variations with two or three colours and one or two sides. I promise to respond to every single submission.

Many thanks and happy new year.

All the best,
Wilfried

Target Market(s)

B2B

Industry/Entity Type

Trade

Contact Information for Business Card

We have successfully designed a logo with ArtFlock and would like now to design our business cards. We would like to keep the colours and the look-and-feel of the logo. Please send in variations with two or three colours and one or two sides. I promise to respond to every single submission.

Font styles to use
Serif
Sans Serif
Script

Requirements
Must have
• These information should be on the business card, grouped as you suggest, and we think using small pictograms for mobile, email, etc is pretty helpful:
• Wilfried Tammler (first and second name)
• Geschäftsführer/ Managing Director (title)
• KoR Warenkontor GmbH (company name and legal form)
• Ostheimer Str. 18/3 (street and house number)
• 71234 Lindenfeld (zip code and town)
• +491709384562 (mobile)
• +4955519027341 (work)
• w.tammler@kor-warenkontor.example (email)
• www.kor-warenkontor.example (web)
Nice to have
• Spectacular and interesting layout and design. You look at it and think, wow, that's not the normal stuff.
• We think of ourselves as bridge-builders between businesses (international producers on the one hand, and retail chains on the other hand) and we translate, organise and manage projects where both partners are involved, but it's difficult for them to cooperate due to language barriers and different working cultures.
• This is why we have the n between the B's shaped as a bridge, and the green arc supports this idea. Maybe you could play with this idea...
Should not have
• the standard layout that everybody has

```html
<!DOCTYPE html>
<html lang="de">
<head>
<meta charset="utf-8">
<title>KoR Warenkontor – Visitenkarten</title>
<link href="https://fonts.googleapis.com/css2?family=Open+Sans:wght@400;600;700&display=swap" rel="stylesheet">
<style>
  :root {
    --green: #2eaa4a;
    --ink: #222222;
    --band: #252525;
    --paper: #ffffff;
    --muted: #555555;
    --rule: #cfcfcf;
    --backdrop: #2a2a2a;
  }
  * { box-sizing: border-box; margin: 0; padding: 0; }
  html, body { width: 1200px; height: 1000px; overflow: hidden; }
  body {
    background: var(--backdrop);
    font-family: "Open Sans", Arial, sans-serif;
    position: relative;
  }
  .card {
    position: absolute;
    width: 600px;
    height: 345px;
    background: var(--paper);
    border-radius: 34px;
    overflow: hidden;
    box-shadow: 0 18px 40px rgba(0,0,0,.45);
  }
  .wordmark {
    font-family: "Open Sans", Arial, sans-serif;
    font-weight: 700;
    letter-spacing: .5px;
    display: flex;
    align-items: center;
    gap: 12px;
    line-height: 1.05;
    white-space: nowrap;
  }
  .wordmark .mark-dot {
    width: 16px; height: 16px; border-radius: 50%;
    background: var(--green); flex: none;
  }

  /* Back side */
  .card-back { left: 90px; top: 90px; }
  .card-back .dark-band {
    position: absolute; left: 90px; right: 0; top: 85px; height: 190px;
    background: var(--band);
  }
  .card-back .green-block {
    position: absolute; left: 0; top: 185px; width: 90px; height: 90px;
    background: var(--green);
  }
  .card-back .wordmark {
    position: absolute; left: 120px; top: 190px;
    color: var(--paper); font-size: 30px;
  }
  .card-back .web {
    position: absolute; right: 40px; top: 110px;
    color: #cfcfcf; font-size: 15px; font-weight: 400; white-space: nowrap;
  }

  /* Front side */
  .card-front { left: 510px; top: 560px; }
  .card-front .wordmark {
    position: absolute; left: 40px; top: 112px;
    color: var(--ink); font-size: 32px;
    flex-direction: column; align-items: flex-start; gap: 4px;
  }
  .card-front .wordmark .line { display: flex; align-items: center; gap: 12px; }
  .identity {
    position: absolute; left: 300px; top: 30px;
    border-left: 4px solid var(--green); padding-left: 12px;
    white-space: nowrap;
  }
  .identity .name {
    font-size: 20px; font-weight: 700; color: var(--ink); letter-spacing: .5px; line-height: 1.15;
  }
  .identity .name .surname { color: var(--green); }
  .identity .title { font-size: 12px; font-weight: 600; color: var(--muted); }
  .contacts {
    position: absolute; left: 300px; top: 108px;
    list-style: none;
    border-left: 2px solid var(--rule); padding-left: 12px;
  }
  .contacts li {
    display: flex; align-items: center; gap: 9px;
    font-size: 12.5px; color: var(--muted); height: 24px;
    white-space: nowrap;
  }
  .contacts .accent { color: var(--green); }
  .icon {
    width: 17px; height: 17px; border-radius: 50%;
    background: var(--green); flex: none;
    display: flex; align-items: center; justify-content: center;
  }
  .icon svg { width: 11px; height: 11px; }
  .address-band {
    position: absolute; left: 0; bottom: 0; width: 370px; height: 66px;
    background: var(--band); color: #e6e6e6;
    font-size: 14px; display: flex; align-items: center; padding-left: 36px;
    white-space: nowrap;
  }
  .company-band {
    position: absolute; right: 0; bottom: 0; width: 230px; height: 105px;
    background: var(--green); color: var(--paper);
    font-size: 13px; font-weight: 700; letter-spacing: 1px;
    display: flex; align-items: center; justify-content: center;
    padding-bottom: 20px; white-space: nowrap;
  }
</style>
</head>
<body>

  <section class="card card-back" aria-label="Visitenkarte Rückseite">
    <div class="dark-band"></div>
    <div class="green-block"></div>
    <div class="wordmark"><span class="mark-dot"></span><span>KoR Warenkontor</span></div>
    <p class="web">www.kor-warenkontor.example</p>
  </section>

  <section class="card card-front" aria-label="Visitenkarte Vorderseite">
    <div class="wordmark">
      <span class="line"><span class="mark-dot"></span>KoR</span>
      <span>Warenkontor</span>
    </div>

    <div class="identity">
      <p class="name">WILFRIED <span class="surname">TAMMLER</span></p>
      <p class="title">Geschäftsführer/Managing Director</p>
    </div>

    <ul class="contacts">
      <li>
        <span class="icon"><svg viewBox="0 0 12 12"><path d="M3 1.5l1.6 2.2-.9 1.1c.6 1.3 1.3 2 2.5 2.5l1.1-.9L9.5 8 8.7 9.8C5 9.7 2.2 7 2 3.3z" fill="#fff"/></svg></span>
        +491709384562
      </li>
      <li>
        <span class="icon"><svg viewBox="0 0 12 12"><rect x="2" y="5" width="8" height="5" rx="1" fill="#fff"/><path d="M1.5 5c0-2 9-2 9 0v.8H8.5V4.5h-5v1.3h-2z" fill="#fff"/></svg></span>
        +4955519027341
      </li>
      <li>
        <span class="icon"><svg viewBox="0 0 12 12"><rect x="1.5" y="3" width="9" height="6" rx=".6" fill="#fff"/><path d="M1.8 3.3L6 6.6l4.2-3.3" stroke="#2eaa4a" stroke-width="1" fill="none"/></svg></span>
        w.tammler@kor-warenkontor.example
      </li>
      <li>
        <span class="icon"><svg viewBox="0 0 12 12"><circle cx="6" cy="6" r="4.3" fill="none" stroke="#fff" stroke-width="1.1"/><path d="M1.7 6h8.6M6 1.7c-2 2.4-2 6.2 0 8.6M6 1.7c2 2.4 2 6.2 0 8.6" stroke="#fff" stroke-width=".9" fill="none"/></svg></span>
        <span>www.<span class="accent">kor-warenkontor</span>.example</span>
      </li>
    </ul>

    <div class="address-band">Ostheimer Str. 18/3, 71234 Lindenfeld</div>
    <div class="company-band">KOR WARENKONTOR GMBH</div>
  </section>

</body>
</html>
```